Tollbury Malt Keller Beer Bottle Label #1

A beer bottle label is required for TMK's first beer that will go on sale later this year.
It is hoped that an on-going relationship will be formed with the successful designer.
Designs for glasses, packaging, t-shirts etc will also be required later this year.
Designs should reflect the local origin of the brewery and project an image of tradition and quality.
Designs should be simple, clean, classic and classy.
Designs should not be loud, bright, crazy or busy.
Design should include an element that can be used as brewery logo.
'Malt Keller' to be prominent, 'Tollbury' to be discreet.
Name of first beer to be Tollmo-Dunkel - label shall be easily adapted for different beers e.g. Tollmo-Weiss.
Deliverables include a smaller text only label for back of the bottle.

***I also need a logo that goes with my label design. So whoever submitted a logo that I like will be selected as the 2nd place winner.

Please refer to the attachment on this brief.

Requirements
Must have
• See uploaded design brief.
Nice to have
Should not have

```html
<!DOCTYPE html>
<html lang="en">
<head>
<meta charset="utf-8">
<title>Tollbury Malt Keller – Tollmo-Dunkel Label</title>
<link rel="stylesheet" href="https://fonts.googleapis.com/css2?family=Rye&family=Roboto+Mono:wght@400;500&family=Montserrat:wght@300;400&display=swap">
<style>
  :root {
    --label-bg: #313131;
    --ink: #f1eee6;
    --ink-muted: #8c8c8c;
    --stripe-dark: #1c1c1c;
    --stripe-light: #f4f2ec;
    --barrel-light: #bdbab3;
    --barrel-dark: #6e6c67;
  }
  * { margin: 0; padding: 0; box-sizing: border-box; }
  html, body {
    width: 1200px; height: 800px; overflow: hidden;
    background: var(--label-bg);
  }
  .label {
    position: relative; width: 1200px; height: 800px;
    background: var(--label-bg); color: var(--ink);
    font-family: "Roboto Mono", monospace;
    overflow: hidden;
  }
  .stripe-band {
    position: absolute; left: 0; width: 100%;
    background: repeating-linear-gradient(90deg,
      var(--stripe-light) 0 11px, var(--stripe-dark) 11px 22px);
  }
  .stripe-band--top { top: 0; height: 30px; }
  .stripe-band--bottom { bottom: 0; height: 32px; }

  .dates {
    position: absolute; left: 72px; top: 84px;
    font-size: 19px; font-weight: 500; line-height: 1.35; letter-spacing: 0.5px;
  }
  .dates .bottled { margin-bottom: 30px; }

  .ingredients {
    position: absolute; left: 66px; top: 280px; height: 330px;
    writing-mode: vertical-rl; transform: rotate(180deg);
    font-size: 17px; text-align: center;
  }

  .brewery-info {
    position: absolute; right: 60px; top: 92px; height: 500px;
    writing-mode: vertical-rl;
    font-size: 17px; line-height: 30px; letter-spacing: 0.3px;
  }

  .brand-mark {
    position: absolute; left: 50%; top: 112px; transform: translateX(-50%);
    display: flex; align-items: center; gap: 12px;
    font-family: "Rye", serif; font-size: 34px; letter-spacing: 2px;
  }
  .brand-mark .mark-square {
    width: 22px; height: 22px; background: var(--ink);
  }

  .title {
    position: absolute; left: 0; width: 100%; top: 288px; text-align: center;
    font-family: "Rye", serif; line-height: 1;
  }
  .title .name { font-size: 62px; letter-spacing: 3px; }
  .title .town { font-size: 40px; letter-spacing: 2px; margin-top: 6px; }

  .barrel-art {
    position: absolute; left: 497px; top: 402px; width: 172px; height: 188px;
    background: radial-gradient(ellipse at 45% 45%, var(--barrel-light), var(--barrel-dark) 80%);
    border-radius: 40px 40px 16px 16px;
  }

  .beer {
    position: absolute; left: 0; width: 100%; top: 617px; text-align: center;
    font-family: "Montserrat", sans-serif; font-weight: 300;
    font-size: 22px; letter-spacing: 3px; line-height: 42px;
  }
  .volume {
    position: absolute; left: 0; width: 100%; top: 714px; text-align: center;
    font-family: "Montserrat", sans-serif; font-weight: 300;
    font-size: 18px; letter-spacing: 1.5px; color: var(--ink-muted);
  }

  .origin {
    position: absolute; left: 910px; width: 220px; top: 652px; text-align: center;
    font-size: 19px; font-weight: 500; line-height: 34px; letter-spacing: 0.5px;
  }
</style>
</head>
<body>
<main class="label">
  <div class="stripe-band stripe-band--top"></div>

  <div class="dates">
    <p class="bottled">BOTTLED JUN' 2018</p>
    <p>BEST BEFORE: 12.06.19.</p>
    <p>(KEEP REFRIGERATED)</p>
  </div>

  <p class="ingredients">Ingredients (Barley, Hops, Water, Yeast)</p>

  <div class="brewery-info">
    <p>TMK. The Brewery . XX8 YY9, England</p>
    <p>High quality beers inspired by tradition and quality</p>
  </div>

  <div class="brand-mark">
    <span class="mark-square"></span>
    <span>TMK</span>
  </div>

  <h1 class="title">
    <span class="name">MALT KELLER'</span><br>
    <span class="town">TOLLBURY</span>
  </h1>

  <div class="barrel-art" role="img" aria-label="Engraved-style wooden beer barrel on a stand with a tap"></div>

  <p class="beer">TOLLMO-DUNKEL<br>PREMIUM LAGER BEER</p>
  <p class="volume">500ML, ABV 4.6%, 2.3 UNITS</p>

  <p class="origin">MADE IN<br>TOLLBURY, ENGLAND.</p>

  <div class="stripe-band stripe-band--bottom"></div>
</main>
</body>
</html>
```